quorvadeal.com redesign with wireframes, white space and custom form are very important

Need a new two column design that will convert easily to mobile responsive. Lots of white space. Winning design will probably be based on header area and making the custom form stand out. I want the header to be very much like www.talbekmo.com except the form not to go up into the header.
Here are some of the websites I really like:
www.pivrostacks.com
http://glendarokfastmove.com/
http://morquilandestate.com/

We buy homes for cash and close fast. Our target is a home seller who is desperate to sell quickly.
I have uploaded my really ugly wireframe and my logo. I also uploaded my photo for the about us box and a possible photo to use for the header.
The copy on the wireframe is what I will be using except for the about us box.

Here is the exact link for video to frame in the top left box.
https://example-vidhost.net/Kp39xqTzR2a

Number of Pages Required

1 page

Font styles to use
Sans Serif

Colors
0592cd
85cae6
eaf1f7
fbee3d
ec1f27

Requirements
Must have
• Everything on wireframe.
• Must use Verdana font and nothing should be smaller than 12 point. Most should be in 14 point. (except maybe inside of form)

```html
<!DOCTYPE html>
<html lang="en">
<head>
<meta charset="utf-8">
<title>quorvadeal.com – Sell Your Home For Cash</title>
<link rel="stylesheet" href="https://fonts.googleapis.com/css2?family=PT+Sans:wght@400;700&display=swap">
<style>
:root{
  --red:#ec1f27;
  --blue:#0592cd;
  --blue-bar:#3a7fe0;
  --pale:#eaf1f7;
  --ink:#111;
  --text:#555;
  --line:#e2e2e2;
  --dark:#2b2b2b;
  --darker:#111;
  --nav:#0d0d0d;
}
*{box-sizing:border-box;margin:0;padding:0}
html,body{width:1200px;height:2206px;overflow:hidden}
body{font-family:Verdana,"PT Sans",sans-serif;color:var(--text);font-size:12px;position:relative}
.backdrop{position:absolute;inset:0;background:linear-gradient(180deg,#f0a86a 0%,#d9895c 12%,#8a7f8a 28%,#5c5e72 45%,#8a7266 65%,#9b7a66 80%,#7d5f50 100%)}
.page{position:absolute;left:190px;top:35px;width:820px;height:2133px;background:#fff}
.header{position:absolute;left:0;top:0;width:820px;height:102px}
.logo{position:absolute;left:20px;top:34px;display:flex;align-items:center;gap:8px;font-size:24px;font-weight:bold;color:var(--red)}
.logo-mark{width:18px;height:18px;background:var(--red)}
.call{position:absolute;left:607px;top:9px;width:194px;height:81px;background:var(--pale);text-align:center;padding-top:10px}
.call b{display:block;color:var(--ink);font-size:16px;letter-spacing:.5px}
.call span{display:block;color:var(--ink);font-size:13px;margin-top:3px}
.call strong{display:block;color:var(--red);font-size:15px;margin-top:4px}
.nav{position:absolute;left:-12px;top:102px;width:844px;height:36px;background:var(--nav);display:flex;align-items:stretch;padding-left:30px}
.nav a{color:#fff;text-decoration:none;font-size:11.5px;display:flex;align-items:center;justify-content:center;border-right:1px solid #444}
.nav a.on{background:var(--red)}
.hero{position:absolute;left:0;top:138px;width:820px;height:228px;background:linear-gradient(180deg,#5d6a72 0%,#8c9aa0 35%,#5f6e3e 65%,#4b5a2a 100%)}
.hero-title{position:absolute;left:128px;top:67px;width:564px;height:73px;background:rgba(255,255,255,.82);text-align:center;padding-top:10px}
.hero-title h1{font-size:24px;color:var(--ink);letter-spacing:.3px}
.hero-title p{font-size:16px;font-weight:bold;color:var(--ink);margin-top:2px}
.box{position:absolute;border:2px solid #ececec;background:#fff;padding:16px 16px}
.box h2{font-size:16.5px;color:var(--ink);line-height:1.3;letter-spacing:.3px}
.ticks{list-style:none;margin-top:10px}
.ticks li{position:relative;padding-left:24px;font-size:11.5px;line-height:22px}
.ticks li svg{position:absolute;left:0;top:6px}
.video{margin-top:10px;width:345px;height:138px;background:linear-gradient(180deg,#cfeff6,#9fd8e4);position:relative}
.video-name{position:absolute;left:0;bottom:0;width:100%;height:45px;background:var(--blue-bar);color:#fff;text-align:center;font-size:14px;line-height:19px;padding-top:4px}
.form p.sub{text-align:center;font-size:11.5px;color:#333;margin:8px 0 14px}
.field{height:32px;border:1px solid #d8d8d8;margin-bottom:10px;font-size:11px;color:#999;padding:9px 10px}
.row2{display:flex;gap:14px}.row2 .field{flex:1}
.agree{display:flex;align-items:center;gap:8px;font-size:11px;color:#555;margin:2px 0 12px}
.agree i{width:14px;height:14px;border:1px solid #aaa;border-radius:2px}
.btn{height:37px;background:var(--red);color:#fff;font-weight:bold;font-size:14.5px;text-align:center;line-height:37px}
.copy{font-size:11.5px;line-height:18px;margin-top:10px}
.copy em{color:var(--red);font-style:normal;font-weight:bold}
.copy strong{display:block;color:var(--ink);margin-top:14px}
.quote{background:#efefef;font-style:italic;font-size:11.5px;line-height:18px;color:#555;padding:10px 22px;margin-top:14px;position:relative}
.quote:after{content:"";position:absolute;left:18px;bottom:-10px;border:6px solid transparent;border-top-color:#efefef;border-left-color:#efefef}
.person{display:flex;align-items:center;gap:10px;margin-top:18px}
.avatar{width:46px;height:46px;border-radius:50%;background:linear-gradient(#c9b59d,#6c5a4a)}
.person b{display:block;color:#222;font-size:12px}
.person span{font-size:11.5px}
.dots{margin-left:auto;display:flex;gap:5px}.dots i{width:8px;height:8px;border-radius:50%;background:#444}.dots i.on{background:var(--red)}
.about{display:flex;gap:20px;margin-top:8px;font-size:11.5px;line-height:18px}
.about-photo{width:80px;height:80px;flex:none;background:linear-gradient(#c3d7e6,#4d5d74);margin-top:-20px}
.post{display:flex;gap:12px;margin-top:18px}
.thumb{width:83px;height:83px;flex:none;background:linear-gradient(#e4e9ec,#6f8a5a)}
.thumb.alt{background:linear-gradient(#cfd6da,#5d4a3c)}
.post .meta{font-size:11.5px;color:#333;display:flex;align-items:center;gap:5px}
.post .meta b{color:#333}
.post p{font-size:11.5px;line-height:18px;margin-top:2px}
.more{color:var(--red);font-size:11.5px;margin-top:18px;display:block;text-decoration:underline}
.cities-intro{font-size:11.5px;line-height:18px;margin-top:8px}
.cities{display:grid;grid-template-columns:136px 115px 1fr;font-size:11.5px;line-height:20.7px;margin-top:6px}
.cities-note{color:var(--red);text-decoration:underline;font-size:11.5px;margin-top:10px;display:block}
.tags{display:flex;flex-wrap:wrap;gap:10px;margin-top:12px;width:360px}
.tags span{border:2px solid #e6e6e6;font-size:11.5px;padding:6px 10px}
.buy-photos{display:flex;gap:6px;margin-top:12px}
.buy-photos div{width:170px;height:67px;background:linear-gradient(#9db5cf,#7a6a58)}
.buy-photos div+div{background:linear-gradient(#d7dde2,#6e5e48)}
.buy-caption{color:#111;font-size:11.5px;margin-top:8px}
.footer{position:absolute;left:0;top:1884px;width:820px;height:215px;background:var(--dark);color:#bbb}
.fcol{position:absolute;top:28px}
.fcol h3{color:#fff;font-size:14px;padding-bottom:8px;border-bottom:1px solid #666;display:inline-block;letter-spacing:.3px}
.fcol p,.fcol li{font-size:11.5px;line-height:19px}
.fcol ul{list-style:none;margin-top:18px}
.fcol .icon{display:inline-block;width:10px;height:10px;background:#ddd;border-radius:50%;margin-right:16px;vertical-align:-1px}
.contact li{display:flex;gap:10px;margin-bottom:8px}
.contact u{color:#fff}
.bottom{position:absolute;left:0;top:2099px;width:820px;height:34px;background:var(--darker);color:#ccc;font-size:11px;display:flex;justify-content:space-between;align-items:center;padding:0 18px 0 22px}
</style>
</head>
<body>
<div class="backdrop" role="img" aria-label="Blurred photo of a house with a paved driveway at sunset"></div>
<div class="page">
  <header class="header">
    <div class="logo"><i class="logo-mark"></i>quorvadeal.com</div>
    <div class="call"><b>CALL US</b><span>Nights and weekends ok</span><strong>555-210-4837</strong></div>
  </header>
  <nav class="nav">
    <a class="on" style="width:78px">HOME</a>
    <a style="width:150px">SELL YOUR HOME</a>
    <a style="width:150px">HOW IT WORKS</a>
    <a style="width:188px">STOP FORECLOSURE</a>
    <a style="width:120px">PROBATE</a>
    <a style="width:124px">CONTACT</a>
  </nav>
  <section class="hero" role="img" aria-label="Photo of a single-storey home with a front porch and hedge">
    <div class="hero-title"><h1>SELL YOUR HOME FOR CASH IN 8 DAYS</h1><p>WE BUY HOUSES NATIONWIDE</p></div>
  </section>

  <section class="box" style="left:19px;top:394px;width:378px;height:408px">
    <h2>THESE ARE THE BENEFITS OF SELLING YOUR HOME TO US.</h2>
    <ul class="ticks">
      <li><svg width="12" height="10"><path d="M1 5l3.5 3.5L11 1" stroke="#ec1f27" stroke-width="2" fill="none"/></svg>You pick the closing date</li>
      <li><svg width="12" height="10"><path d="M1 5l3.5 3.5L11 1" stroke="#ec1f27" stroke-width="2" fill="none"/></svg>You pay NO commissions or fees</li>
      <li><svg width="12" height="10"><path d="M1 5l3.5 3.5L11 1" stroke="#ec1f27" stroke-width="2" fill="none"/></svg>You don't have to paint, clean or make repairs</li>
    </ul>
    <p class="copy" style="color:#111;margin-top:16px">Watch to see our president Dale explain how easy it is to sell to us.</p>
    <div class="video" role="img" aria-label="Video still of the company president">
      <svg width="60" height="60" style="position:absolute;left:142px;top:42px"><circle cx="30" cy="30" r="27" fill="rgba(255,255,255,.35)" stroke="#fff" stroke-width="3"/><path d="M23 17l19 13-19 13z" fill="#fff"/></svg>
      <div class="video-name">Dale Morrow<br>Quorvadeal.com</div>
    </div>
  </section>

  <section class="box form" style="left:422px;top:394px;width:379px;height:408px">
    <h2 style="text-align:center">YES, I WANT TO SELL MY HOME FAST!</h2>
    <p class="sub">Get a no obligation written offer in 36 hours</p>
    <div class="row2"><div class="field">Name</div><div class="field">Phone</div></div>
    <div class="field">Email</div>
    <div class="field">Address including City, State and Zip Code</div>
    <div class="field">Repairs needed if any</div>
    <div class="field">Asking price</div>
    <div class="field">Comments</div>
    <div class="agree"><i></i>Agree With Our Terms &amp; Conditions</div>
    <div class="btn">Get Started Selling Your Home Fast</div>
  </section>

  <section class="box" style="left:19px;top:830px;width:378px;height:378px">
    <h2>WE BUY HOUSES AND CLOSE QUICKLY</h2>
    <p class="copy">Selling a home on your own has never been easier. From Orlando to Greensboro - and all points in be-tween- you can sell your home today without any hassles. <em>Call 1-800-555-0142</em> or fill out the form below to get a written offer on your home in just 36 hours. Sell today online to people that care.<strong>If you need to sell a home fast because of:</strong></p>
    <ul class="ticks" style="margin-top:12px">
      <li><svg width="12" height="10"><path d="M1 5l3.5 3.5L11 1" stroke="#ec1f27" stroke-width="2" fill="none"/></svg>Divorce or Bankruptcy</li>
      <li><svg width="12" height="10"><path d="M1 5l3.5 3.5L11 1" stroke="#ec1f27" stroke-width="2" fill="none"/></svg>Foreclosure</li>
      <li><svg width="12" height="10"><path d="M1 5l3.5 3.5L11 1" stroke="#ec1f27" stroke-width="2" fill="none"/></svg>Landlord problems - evictions with tenants okay</li>
      <li><svg width="12" height="10"><path d="M1 5l3.5 3.5L11 1" stroke="#ec1f27" stroke-width="2" fill="none"/></svg>Inherited property in probate</li>
      <li><svg width="12" height="10"><path d="M1 5l3.5 3.5L11 1" stroke="#ec1f27" stroke-width="2" fill="none"/></svg>Termites, mold, flood or fire damage, leaky roof</li>
      <li><svg width="12" height="10"><path d="M1 5l3.5 3.5L11 1" stroke="#ec1f27" stroke-width="2" fill="none"/></svg>Moving or can't afford mortgage payments</li>
    </ul>
  </section>

  <section class="box" style="left:422px;top:830px;width:379px;height:232px">
    <h2>HOME SELLER TESTIMONIALS</h2>
    <p class="quote">I just wanted to thank you for buying my home in Winter Park. You made it fast and easy and kept me well informed the whole way.</p>
    <div class="person"><div class="avatar" role="img" aria-label="Customer portrait"></div><div><b>JONATHAN DOE</b><span>Lorem Ipsum</span></div><div class="dots"><i></i><i class="on"></i><i></i></div></div>
  </section>

  <section class="box" style="left:422px;top:1087px;width:379px;height:121px">
    <h2>ABOUT US</h2>
    <div class="about"><p>Owned and operated in Orlando Florida since 2001. Oldest Continuous operated website in country.</p><div class="about-photo" role="img" aria-label="Portrait of the owner"></div></div>
  </section>

  <section class="box" style="left:19px;top:1233px;width:378px;height:441px">
    <h2>RECENT BLOG POSTS</h2>
    <div class="post"><div class="thumb" role="img" aria-label="Model house held in hands"></div><div><div class="meta">◷ April 8th, 2015 💬 <b>10 Comments</b></div><p>Lorem ipsum dolor sit amet, consectetur adipiscing elit. Aenean libero tortor, auctor et blandit in, facilisis sed nulla. Vivamus condimentum ornare egestas.</p></div></div>
    <div class="post"><div class="thumb alt" role="img" aria-label="Modern house exterior"></div><div><div class="meta">◷ April 10th, 2015 💬 <b>12 Comments</b></div><p>Lorem ipsum dolor sit amet, consectetur adipiscing elit. Aenean libero tortor, auctor et blandit in, facilisis sed nulla. Vivamus condimentum ornare egestas.</p></div></div>
    <div class="post"><div class="thumb" role="img" aria-label="Model house held in hands"></div><div><div class="meta">◷ April 8th, 2015 💬 <b>10 Comments</b></div><p>Lorem ipsum dolor sit amet, consectetur adipiscing elit. Aenean libero tortor, auctor et blandit in, facilisis sed nulla. Vivamus condimentum ornare egestas.</p></div></div>
    <a class="more">View All...</a>
  </section>

  <section class="box" style="left:422px;top:1233px;width:379px;height:441px">
    <h2>SOME OF THE CITIES WHERE WE BUY HOUSES. NOT ALL ARE LISTED</h2>
    <p class="cities-intro">These are the cities where we have an affiliate where you can sell a home fast or quickly and we buy homes:</p>
    <div class="cities">
      <div>Orlando<br>Jacksonville<br>Ft Myers<br>Tampa<br>St Pete<br>Gainesville<br>Tallahassee<br>Melbourne<br>West Palm Beach<br>Apopka<br>Deland<br>Kissimmee<br>Camden Atlanta</div>
      <div>Valdosta<br>Houston<br>Detroit<br>Phoenix<br>Seattle<br>Tacoma<br>Portland<br>Lakeland<br>Ocala<br>Chicago<br>Philadelphia<br>Charlotte<br>Cincinnati</div>
      <div>San Antonio<br>Harrisburg<br>Virginia Beach<br>Virginia Homes<br>Greensboro<br>Charleston SC<br>Flint Rochester<br>Lake Florida<br>Wilmington<br>Columbia<br>Titusville</div>
    </div>
    <a class="cities-note">If you don't see your city, we still probably buy homes there.</a>
  </section>

  <section class="box" style="left:19px;top:1699px;width:378px;height:154px">
    <h2>ARCHIVES</h2>
    <div class="tags"><span>Sell my house</span><span>Fast cash for homes</span><span>Latest News</span><span>Real Estate investor</span><span>We buy houses</span></div>
  </section>

  <section class="box" style="left:422px;top:1699px;width:379px;height:154px">
    <h2>WE BUY</h2>
    <div class="buy-photos"><div role="img" aria-label="Large two-storey house at dusk"></div><div role="img" aria-label="Small bungalow with a porch"></div></div>
    <p class="buy-caption">We buy nice pretty houses and some ugly ones as well.</p>
  </section>

  <footer class="footer">
    <div class="fcol" style="left:25px;width:180px"><h3>WHY US</h3><p style="margin-top:18px">Lorem ipsum dolor sit amet, consectetur adipiscing elit. Aenean libero tortor, auctor et blandit in, facilisis sed nulla. Vivamus condimentum</p></div>
    <div class="fcol" style="left:280px"><h3>SITE LINKS</h3><ul><li>Sell Your Home</li><li>How it works</li><li>Stop foreclosure</li><li>Probate</li><li>Contact</li></ul></div>
    <div class="fcol" style="left:458px"><h3>GET SOCIAL</h3><ul><li><i class="icon"></i>Pagebook</li><li><i class="icon"></i>Chirper</li><li><i class="icon"></i>Circles+</li><li><i class="icon"></i>Linkwork</li></ul></div>
    <div class="fcol contact" style="left:630px;width:180px"><h3>STAY IN TOUCH</h3><ul>
      <li><svg width="10" height="14" style="flex:none;margin-top:3px"><path d="M5 0a5 5 0 0 1 5 5c0 4-5 9-5 9S0 9 0 5a5 5 0 0 1 5-5z" fill="#ddd"/><circle cx="5" cy="5" r="2" fill="#2b2b2b"/></svg><span>4410 Brindle Ave #312 Larkspur Park FL 32700</span></li>
      <li><svg width="11" height="11" style="flex:none;margin-top:4px"><path d="M2 0l3 3-1.5 2a7 7 0 0 0 2.5 2.5L8 6l3 3-2 2C4 11 0 7 0 2z" fill="#ddd"/></svg><span>555-210-4837</span></li>
      <li><svg width="12" height="9" style="flex:none;margin-top:5px"><rect width="12" height="9" fill="#ddd"/><path d="M0 0l6 5 6-5" stroke="#2b2b2b" fill="none"/></svg><u>dale@quorvadeal.com</u></li>
    </ul></div>
  </footer>
  <div class="bottom"><span>Copyright © 2015 . Quorvadeal All right Reserved</span><span>Privacy Policy | Terms &amp; Conditions</span></div>
</div>
</body>
</html>
```